Korvane Motors business cards

We need business cards for our company Korvane Motors, based in Brisbane but trading world wide. We buy and sell Korvane Motors, generators and marine equipment. The design needs to be kept clean, simple but eye catching.
Please keep with our current logo (included) and further information can be included on request

Business

0792cd
33a6d7
85cae6
3276b5
0455a3
cedeed
cee9f5
ffffff

```html
<!DOCTYPE html>
<html lang="en">
<head>
<meta charset="utf-8">
<title>Korvane Motors – Business Cards</title>
<link href="https://fonts.googleapis.com/css2?family=Roboto:wght@400;500&family=Open+Sans:wght@400;600;700&display=swap" rel="stylesheet">
<style>
  :root {
    --backdrop: #5e4230;
    --card-white: #ffffff;
    --brand-blue: #3a7fc1;
    --card-blue: #4a86c0;
    --text-grey: #666a6e;
    --rule-grey: #9a9ea3;
  }
  html, body {
    margin: 0;
    padding: 0;
    width: 1200px;
    height: 1000px;
    overflow: hidden;
    background: var(--backdrop);
  }
  .canvas {
    position: relative;
    width: 1200px;
    height: 1000px;
  }
  .card {
    position: absolute;
    left: 265px;
    width: 665px;
    height: 397px;
    border-radius: 24px;
    overflow: hidden;
  }
  .card-front { top: 73px; background: var(--card-white); }
  .card-back { top: 532px; background: var(--card-blue); }

  .brand {
    position: absolute;
    font-family: "Roboto", sans-serif;
    font-weight: 400;
  }
  .brand-square {
    position: absolute;
    border-radius: 10px;
  }
  .front-square { left: 39px; top: 45px; width: 102px; height: 83px; background: var(--brand-blue); }
  .front-brand {
    left: 153px; top: 40px;
    color: var(--brand-blue);
    font-size: 44px;
    line-height: 46px;
  }
  .front-brand .legal {
    display: block;
    text-align: right;
    font-size: 15px;
    line-height: 18px;
  }

  .person-name {
    position: absolute;
    left: 39px; top: 200px;
    font-family: "Open Sans", sans-serif;
    font-weight: 700;
    font-size: 20px;
    color: var(--brand-blue);
    margin: 0;
  }
  .name-rule-strong {
    position: absolute; left: 39px; top: 227px; width: 155px; height: 3px; background: var(--brand-blue);
  }
  .name-rule-light {
    position: absolute; left: 199px; top: 228px; width: 427px; height: 1px; background: var(--rule-grey);
  }

  .contact-list {
    position: absolute;
    left: 39px; top: 250px;
    margin: 0; padding: 0;
    list-style: none;
    font-family: "Open Sans", sans-serif;
    font-size: 15px;
    color: var(--text-grey);
  }
  .contact-list li {
    display: flex;
    align-items: center;
    height: 20.7px;
  }
  .contact-list svg { width: 12px; height: 12px; margin-right: 8px; fill: var(--brand-blue); }
  .contact-list .accent { color: var(--brand-blue); }

  .address-block {
    position: absolute;
    right: 39px; top: 239px;
    text-align: right;
    font-family: "Open Sans", sans-serif;
    font-size: 15px;
    line-height: 19px;
    color: var(--text-grey);
  }
  .address-block h3 {
    margin: 0;
    font-size: 15px;
    font-weight: 600;
    color: var(--brand-blue);
  }
  .address-block p { margin: 0 0 6px; }

  .back-square { left: 115px; top: 120px; width: 151px; height: 124px; background: var(--card-white); border-radius: 14px; }
  .back-brand {
    left: 285px; top: 110px;
    color: var(--card-white);
    font-size: 70px;
    line-height: 72px;
  }
  .back-brand .legal {
    display: block;
    text-align: right;
    font-size: 22px;
    line-height: 24px;
  }
  .back-web {
    position: absolute;
    left: 0; right: 0; top: 333px;
    text-align: center;
    font-family: "Open Sans", sans-serif;
    font-size: 16px;
    color: var(--card-white);
  }
  .back-web strong { font-weight: 700; }
</style>
</head>
<body>
<main class="canvas">
  <section class="card card-front">
    <div class="brand-square front-square"></div>
    <div class="brand front-brand">Korvane<br>Motors<span class="legal">Pty Ltd</span></div>

    <h2 class="person-name">Marla Henshaw</h2>
    <div class="name-rule-strong"></div>
    <div class="name-rule-light"></div>

    <ul class="contact-list">
      <li><svg viewBox="0 0 12 12"><path d="M3 0h6v12H3z M4 1v9h4V1z"/></svg>+61 455 208 914</li>
      <li><svg viewBox="0 0 12 12"><path d="M1 4c0-2 2-3 5-3s5 1 5 3v1H8V4H4v1H1z M2 6h8l1 5H1z"/></svg>+61 7 3624 5180</li>
      <li><svg viewBox="0 0 12 12"><path d="M3 0h6v4H3z M0 4h12v5H10v3H2V9H0z M3 8v3h6V8z"/></svg>+61 7 3624 5199</li>
      <li><svg viewBox="0 0 12 12"><path d="M0 2h12v8H0z M1 3l5 4 5-4v-.2H1z" /></svg>marla@korvane-motors.com.au</li>
      <li><svg viewBox="0 0 12 12"><path d="M6 0a6 6 0 1 0 0 12A6 6 0 1 0 6 0z M6 1.5a4.5 4.5 0 1 1 0 9a4.5 4.5 0 1 1 0-9z M1 5.5h10v1H1z M5.5 1h1v10h-1z"/></svg>www.<span class="accent">korvane-motors</span>.com.au</li>
    </ul>

    <div class="address-block">
      <h3>Adress Location</h3>
      <p>14 Tallowood Street<br>HARTWELL QLD 4179</p>
      <h3>Postal Address</h3>
      <p>PO Box 582,<br>Corrigan QLD 4168</p>
    </div>
  </section>

  <section class="card card-back">
    <div class="brand-square back-square"></div>
    <div class="brand back-brand">Korvane<br>Motors<span class="legal">Pty Ltd</span></div>
    <div class="back-web">www.<strong>korvane-motors</strong>.com.au</div>
  </section>
</main>
</body>
</html>
```